law firm business cards

I need a business card using my existing logo. Two sided is best because there is a lot of information that needs to go on the card. Use the same general color scheme as logo, but I need one set with the blue background of my website (www.kestonlegalgroup.com), and one set with white background (to see which one I like best).

Information that must be on there:
Darren P. Holloway
Board Certified Civil Trial Specialist
738 Brindlewood Ave., Suite 2300
Raleigh, NC 27699

T 919-555-0142
F 919-555-0187

www.kestonlegalgroup.com
darren@kestonlegalgroup.com

Personal Injury | Criminal Law (to separate the two, pls use a bullet point or pipeline symbol "|"

If there is a way to work in the QRVC logo (maybe at the bottom somewhere), put it in, but don't let it detract from the main logo too much.

Also, if there is a way to work it in, put in somewhere: Former Insurance Company Attorney | Former Criminal Prosecutor (to separate the two, pls use a bullet point or pipeline symbol "|"

```html
<!DOCTYPE html>
<html lang="en">
<head>
<meta charset="utf-8">
<title>Keston Legal – Business Cards</title>
<link href="https://fonts.googleapis.com/css2?family=Crimson+Text:wght@400;600&display=swap" rel="stylesheet">
<style>
  :root {
    --navy: #1b3573;
    --navy-deep: #0f2558;
    --navy-light: #27468c;
    --paper: #ffffff;
    --stage: #eceef2;
    --ink: #1c2f66;
    --accent-red: #d21f2e;
    --silver: #e9edf3;
  }
  * { box-sizing: border-box; margin: 0; padding: 0; }
  html, body {
    width: 1200px;
    height: 1000px;
    overflow: hidden;
    background: var(--stage);
    font-family: "Crimson Text", Georgia, serif;
  }
  .canvas {
    position: relative;
    width: 1200px;
    height: 1000px;
  }
  .card {
    position: absolute;
    width: 700px;
    height: 400px;
    box-shadow: 0 10px 28px rgba(15, 37, 88, 0.22);
    overflow: hidden;
  }
  .accent-curve {
    position: absolute;
    left: 0;
    top: 0;
    width: 100%;
    height: 100%;
    pointer-events: none;
  }
  .accent-curve path {
    fill: none;
    stroke: var(--accent-red);
    stroke-linecap: round;
  }

  /* Front side */
  .card-front {
    left: 80px;
    top: 60px;
    background: linear-gradient(160deg, var(--navy-light) 0%, var(--navy) 45%, var(--navy-deep) 100%);
  }
  .front-brand {
    position: absolute;
    left: 60px;
    top: 120px;
    display: flex;
    align-items: center;
    gap: 26px;
  }
  .front-brand .brand-mark {
    width: 70px;
    height: 70px;
    background: var(--silver);
  }
  .front-brand .brand-name {
    font-size: 62px;
    font-weight: 400;
    letter-spacing: 3px;
    text-transform: uppercase;
    color: var(--silver);
    line-height: 1;
  }

  /* Back side */
  .card-back {
    left: 420px;
    top: 540px;
    background: var(--paper);
  }
  .back-brand {
    position: absolute;
    left: 34px;
    top: 26px;
    display: flex;
    align-items: center;
    gap: 12px;
  }
  .back-brand .brand-mark {
    width: 30px;
    height: 30px;
    border-radius: 50%;
    background: var(--navy);
  }
  .back-brand .brand-name {
    font-size: 32px;
    font-weight: 400;
    letter-spacing: 1.5px;
    text-transform: uppercase;
    color: var(--navy);
    line-height: 1;
  }
  .attorney {
    position: absolute;
    left: 60px;
    top: 120px;
    color: var(--ink);
    font-size: 20px;
    line-height: 1.3;
  }
  .cert-badge {
    position: absolute;
    left: 40px;
    top: 232px;
    width: 74px;
    height: 74px;
    border-radius: 50%;
    border: 3px solid var(--ink);
    background: var(--paper);
  }
  .web-contact {
    position: absolute;
    left: 130px;
    top: 240px;
    color: var(--ink);
    font-size: 18px;
    line-height: 1.55;
  }
  .info-column {
    position: absolute;
    right: 0;
    top: 0;
    width: 300px;
    height: 100%;
    display: flex;
    flex-direction: column;
    gap: 12px;
    background: var(--paper);
  }
  .info-column .band {
    background: var(--navy);
    color: var(--paper);
  }
  .band-top { height: 70px; }
  .band-main {
    flex: 1;
    padding: 28px 22px;
    font-size: 17px;
    line-height: 1.45;
    white-space: nowrap;
  }
  .band-main .phones { margin-top: 22px; }
  .band-bottom {
    height: 70px;
    display: flex;
    align-items: center;
    justify-content: center;
    font-size: 17px;
    letter-spacing: 0.5px;
    white-space: nowrap;
  }
</style>
</head>
<body>
<main class="canvas">

  <section class="card card-front" aria-label="Business card front">
    <svg class="accent-curve" viewBox="0 0 700 400" aria-hidden="true">
      <path d="M40 222 Q 330 200 600 282" stroke-width="4"/>
    </svg>
    <div class="front-brand">
      <span class="brand-mark"></span>
      <span class="brand-name">Keston Legal</span>
    </div>
  </section>

  <section class="card card-back" aria-label="Business card back">
    <svg class="accent-curve" viewBox="0 0 700 400" aria-hidden="true">
      <path d="M30 72 Q 230 62 390 96" stroke-width="2.5"/>
    </svg>
    <div class="back-brand">
      <span class="brand-mark"></span>
      <span class="brand-name">Keston Legal</span>
    </div>

    <div class="attorney">
      <p class="attorney-name">Darren P. Holloway</p>
      <p class="attorney-title">Board Certified Civil Trial Specialist</p>
    </div>

    <div class="cert-badge" role="img" aria-label="Board certification badge"></div>

    <div class="web-contact">
      <p>www.kestonlegalgroup.com</p>
      <p>darren@kestonlegalgroup.com</p>
    </div>

    <aside class="info-column">
      <div class="band band-top"></div>
      <div class="band band-main">
        <p>738 Brindlewood Ave., Suite 2300</p>
        <p>Raleigh, NC 27699</p>
        <div class="phones">
          <p>T 919-555-0142</p>
          <p>F 919-555-0187</p>
        </div>
      </div>
      <div class="band band-bottom">
        <p class="practice-areas">Personal Injury | Criminal Law</p>
      </div>
    </aside>
  </section>

</main>
</body>
</html>
```